Modern Business Card

Modern professional business card with more than just logo and demographic info. Something memorable.

We are a trendy/modern chiropractic group with an emphasis on neurology, hence the minimalist-type brain logo. We want to convey that modern and technical aspect with professionalism and the elite nature of our practice environment.

```html
<!DOCTYPE html>
<html lang="en">
<head>
<meta charset="utf-8">
<title>Kinetic Chiropractic — Business Card</title>
<link rel="stylesheet" href="https://fonts.googleapis.com/css2?family=Crimson+Text:wght@400&family=Titillium+Web:wght@300;400;600&display=swap">
<style>
  :root {
    --backdrop: #e8e4de;
    --card-top: #12161c;
    --card-bottom: #050608;
    --ink-white: #f4f4f4;
    --ink-grey: #8a8d92;
    --ink-soft: #9a9da2;
    --accent: #5e8ac4;
    --accent-soft: #6d95cc;
    --rule: #d8d8d8;
  }
  * { margin: 0; padding: 0; box-sizing: border-box; }
  html, body { width: 1200px; height: 859px; overflow: hidden; }
  body {
    background: var(--backdrop);
    position: relative;
    font-family: "Titillium Web", sans-serif;
  }
  .card {
    position: absolute;
    top: 288px;
    width: 500px;
    height: 285px;
    background: linear-gradient(160deg, var(--card-top), var(--card-bottom));
    box-shadow: 0 10px 24px rgba(0,0,0,0.25);
    overflow: hidden;
  }
  .card--front { left: 59px; }
  .card--back { left: 640px; }

  .accent-band {
    position: absolute;
    top: 0;
    width: 124px;
    height: 100%;
    background: linear-gradient(180deg, var(--accent-soft), var(--accent));
  }
  .card--front .accent-band { left: 368px; }
  .card--back .accent-band { left: 7px; }

  .wordmark {
    position: absolute;
    left: 28px;
    top: 32px;
    font-family: "Crimson Text", serif;
    line-height: 0.9;
  }
  .wordmark__main { display: block; font-size: 30px; letter-spacing: 0.5px; color: var(--ink-white); }
  .wordmark__sub { display: block; font-size: 16.5px; letter-spacing: 0.6px; color: var(--ink-grey); }

  .person { position: absolute; left: 28px; top: 124px; }
  .person__name {
    font-family: "Crimson Text", serif;
    font-size: 19px;
    color: var(--ink-grey);
    letter-spacing: 0.4px;
    line-height: 1.1;
  }
  .person__role {
    font-size: 13px;
    color: var(--accent);
    line-height: 1.2;
  }
  .divider {
    position: absolute;
    left: 28px;
    top: 180px;
    width: 149px;
    height: 1px;
    background: var(--rule);
  }
  .contact {
    position: absolute;
    left: 28px;
    top: 196px;
    list-style: none;
  }
  .contact__item {
    display: flex;
    align-items: center;
    gap: 6px;
    height: 17.5px;
    font-size: 12.5px;
    font-weight: 300;
    color: var(--ink-soft);
  }
  .contact__item svg { width: 12px; height: 12px; flex: none; }
  .contact__highlight { color: var(--accent); font-weight: 600; }

  .brand-lockup {
    position: absolute;
    right: 61px;
    top: 120px;
    display: flex;
    align-items: center;
    gap: 12px;
  }
  .brand-lockup__dot {
    width: 22px;
    height: 22px;
    border-radius: 50%;
    background: var(--accent);
  }
  .brand-lockup__name {
    font-family: "Crimson Text", serif;
    line-height: 0.9;
  }
  .brand-lockup__main { display: block; font-size: 33px; letter-spacing: 0.5px; color: var(--ink-white); }
  .brand-lockup__sub { display: block; font-size: 18.5px; letter-spacing: 0.6px; color: var(--ink-grey); }
</style>
</head>
<body>

<section class="card card--front" aria-label="Card front">
  <div class="wordmark">
    <span class="wordmark__main">KINETIC</span>
    <span class="wordmark__sub">CHIROPRACTIC</span>
  </div>

  <div class="person">
    <p class="person__name">DANIEL HAYES</p>
    <p class="person__role">Training Specialist</p>
  </div>

  <div class="divider"></div>

  <ul class="contact">
    <li class="contact__item">
      <svg viewBox="0 0 12 12" aria-hidden="true"><circle cx="6" cy="6" r="5.2" fill="none" stroke="#5e8ac4" stroke-width="1"/><path d="M4 3.3l1 1.4-.6.7c.4.9 1.1 1.6 2 2l.7-.6 1.4 1-.5 1c-2.2-.2-4.2-2.2-4.4-4.4z" fill="#5e8ac4"/></svg>
      <span>555.014.2290</span>
    </li>
    <li class="contact__item">
      <svg viewBox="0 0 12 12" aria-hidden="true"><rect x="0.8" y="2.5" width="10.4" height="7" fill="none" stroke="#5e8ac4" stroke-width="1"/><path d="M1 3l5 3.6L11 3" fill="none" stroke="#5e8ac4" stroke-width="1"/></svg>
      <span>d.hayes@kineticchiro.com</span>
    </li>
    <li class="contact__item">
      <svg viewBox="0 0 12 12" aria-hidden="true"><circle cx="6" cy="6" r="5.2" fill="none" stroke="#5e8ac4" stroke-width="1"/><ellipse cx="6" cy="6" rx="2.3" ry="5.2" fill="none" stroke="#5e8ac4" stroke-width="0.9"/><path d="M0.8 6h10.4M1.6 3.5h8.8M1.6 8.5h8.8" stroke="#5e8ac4" stroke-width="0.8"/></svg>
      <span>www.<span class="contact__highlight">kineticchiro</span>.com</span>
    </li>
  </ul>

  <div class="accent-band" role="img" aria-label="Brand accent band"></div>
</section>

<section class="card card--back" aria-label="Card back">
  <div class="accent-band" role="img" aria-label="Brand accent band"></div>

  <div class="brand-lockup">
    <div class="brand-lockup__dot"></div>
    <div class="brand-lockup__name">
      <span class="brand-lockup__main">KINETIC</span>
      <span class="brand-lockup__sub">CHIROPRACTIC</span>
    </div>
  </div>
</section>

</body>
</html>
```